Top Real Estate teams new cards UPDATED

New Cards with MY (Im the tall guy in the middle) new pic on the front of card and my team pic on the back of card. Also my team name on the front of the card (marlow and partners) and brokerage name on the back (harborline real estate group) . Also the tag line "Ask about our 20 step plan" on the back of the card and "Welcome to the new way of Real Estate Sales" on the front of the card along with my phone number (951-284-7310) and email address (devon.marlow47@quillmail.net) my website (www.DevonMarlow.org) and my License number (BRE:07315942). I do like my team name colors of black and gold
Logo links are attached:
1. https://www.filecrate.net/sh/918kqwz72pavdle/AAF7QmR2HtK4BnYwPzLxUe_KGb?dl=0
2. https://www.filecrate.net/sh/27w5xvn81rbt094/AACKTJMR46DnQ2Wf7RyGs8Vh3b?dl=0
Updates

Target Market(s)

Real Estate Customers

Industry/Entity Type

Real Estate

Contact Information for Business Card

Classy, yet east ro read and understand

Font styles to use
Sans Serif

Requirements
Must have
• Team and brokerage name, and both slogans.
• Black and gold color scheme.
Nice to have
• Bold writing
Should not have
• cluttered feeling

```html
<!DOCTYPE html>
<html lang="en">
<head>
<meta charset="UTF-8">
<title>Marlow and Partners – Business Cards</title>
<link href="https://fonts.googleapis.com/css2?family=Arimo:ital,wght@0,400;0,700;1,400&display=swap" rel="stylesheet">
<style>
  :root {
    --gold: #c49b25;
    --gold-deep: #b08a1c;
    --ink: #1d1b1c;
    --charcoal: #2a2627;
    --grey-text: #4a4a4a;
    --paper: #ffffff;
    --backdrop: #e9e7e4;
  }
  * { box-sizing: border-box; margin: 0; padding: 0; }
  html, body {
    width: 1200px; height: 950px; overflow: hidden;
    background: var(--backdrop);
    font-family: "Arimo", Arial, sans-serif;
  }
  .sheet { position: relative; width: 1200px; height: 950px; }

  .card {
    position: absolute; left: 215px; width: 770px; height: 440px;
    overflow: hidden; box-shadow: 0 6px 18px rgba(0,0,0,.18);
  }

  /* Front */
  .card-front { top: 25px; background: var(--paper); }
  .front-band { position: absolute; inset: 0; }

  .brand {
    position: absolute; left: 44px; top: 58px;
    display: flex; align-items: center; gap: 18px;
  }
  .brand-dot {
    width: 58px; height: 58px; border-radius: 50%;
    background: var(--charcoal); flex: none;
  }
  .brand-name {
    font-weight: 400; font-size: 38px; line-height: 1.08;
    letter-spacing: 2px; text-transform: uppercase; color: var(--grey-text);
  }

  .contact {
    position: absolute; left: 44px; top: 196px;
    font-size: 17px; line-height: 1.55; color: var(--grey-text);
  }
  .contact .label { color: var(--gold); font-weight: 700; }

  .portrait {
    position: absolute; left: 478px; top: 22px; width: 244px; height: 176px;
    border-radius: 16px; border: 3px solid var(--charcoal);
    background: radial-gradient(circle at 50% 45%, #c9c9c9, #8f8f8f);
  }
  .agent {
    position: absolute; right: 48px; top: 206px; text-align: right;
  }
  .agent-name { font-size: 27px; font-weight: 700; color: var(--ink); line-height: 1.1; }
  .agent-role { font-size: 17px; color: var(--gold); margin-top: 3px; }

  .welcome {
    position: absolute; right: 40px; bottom: 20px; text-align: right;
    color: var(--paper); font-size: 16px; font-weight: 700; letter-spacing: .3px;
  }

  /* Back */
  .card-back { top: 485px; background: var(--gold); color: var(--paper); }
  .back-brand {
    position: absolute; left: 0; right: 0; top: 128px; text-align: center;
  }
  .back-brand .brand-name {
    color: var(--paper); font-size: 50px; letter-spacing: 3px;
  }
  .tagline {
    position: absolute; left: 0; right: 0; top: 268px; text-align: center;
    font-style: italic; font-size: 20px;
  }
  .brokerage {
    position: absolute; right: 34px; bottom: 28px;
    font-size: 14px; letter-spacing: 1px; text-transform: uppercase;
  }
</style>
</head>
<body>
<main class="sheet">

  <section class="card card-front" aria-label="Business card front">
    <svg class="front-band" viewBox="0 0 770 440" preserveAspectRatio="none" aria-hidden="true">
      <path d="M0 440 L0 430 C 200 425, 420 385, 770 280 L770 440 Z" fill="var(--ink)"/>
      <path d="M0 414 C 200 409, 420 367, 770 262" fill="none" stroke="var(--gold)" stroke-width="6"/>
    </svg>

    <div class="brand">
      <span class="brand-dot"></span>
      <span class="brand-name">Marlow and<br>Partners</span>
    </div>

    <div class="contact">
      <p>BRE: 07315942</p>
      <p><span class="label">PHONE:</span> (951-284-7310)</p>
      <p>devon.marlow47@quillmail.net</p>
      <p>www.DevonMarlow.org</p>
    </div>

    <div class="portrait" role="img" aria-label="Portrait photo of the agent"></div>
    <div class="agent">
      <p class="agent-name">Devon Marlow</p>
      <p class="agent-role">Owner</p>
    </div>

    <p class="welcome">Welcome to the new way of Real Estate Sales</p>
  </section>

  <section class="card card-back" aria-label="Business card back">
    <div class="back-brand">
      <span class="brand-name">Marlow and<br>Partners</span>
    </div>
    <p class="tagline">Ask about our 20 step plan</p>
    <p class="brokerage">Harborline Real Estate Group</p>
  </section>

</main>
</body>
</html>
```